Harbor Key Realty - New Agent Opportunity Overview

We want to create a one (1) page brochure to highlight what Harbor Key Realty (a real estate brokerage) offers new agents. I have uploaded a Word doc that has all the text we want on the flyer. We want a professional looking design.
Industry/Entity Type
Real Estate Agent
Colors
3176b5
33a6d7

```html
<!DOCTYPE html>
<html lang="en">
<head>
<meta charset="utf-8">
<title>Harbor Key Realty – New Agent Opportunity</title>
<link href="https://fonts.googleapis.com/css2?family=Arimo:wght@400;700&family=Tinos:wght@400;700&display=swap" rel="stylesheet">
<style>
:root{
  --blue:#3176b5;
  --sky:#33a6d7;
  --deep:#1f5f9e;
  --ink:#111;
  --text:#2a2a2a;
  --paper:#f4f7fa;
  --white:#fff;
}
*{margin:0;padding:0;box-sizing:border-box}
html,body{width:902px;height:1200px;overflow:hidden;background:var(--white)}
.flyer{position:relative;width:902px;height:1200px;overflow:hidden;background:linear-gradient(180deg,#fff 0%,var(--paper) 100%);font-family:"Arimo",Arial,sans-serif;color:var(--text)}
.hero-photo{position:absolute;left:0;top:90px;width:902px;height:470px;background:linear-gradient(170deg,#dfe8f0 0%,#b9cbdc 35%,#7d98b4 65%,#cfdce8 100%)}
.hero-shapes{position:absolute;left:0;top:0;width:902px;height:600px}
.contact{position:absolute;left:26px;top:20px;color:var(--white);font-family:"Tinos",serif;font-weight:700;font-size:17px;line-height:26px}
.brand{position:absolute;left:548px;top:150px;width:282px;height:56px;background:var(--white);border:3px solid var(--deep);display:flex;align-items:center;justify-content:center;font-family:"Arimo",sans-serif;font-weight:700;font-size:24px;letter-spacing:2px;color:var(--deep)}
.headline{position:absolute;left:0;width:902px;top:300px;text-align:center;font-family:"Tinos",serif;font-weight:700;font-size:35px;line-height:48px;color:var(--ink)}
.pitch{position:absolute;left:0;width:902px;top:592px;text-align:center;color:var(--blue);font-weight:700;font-size:31px;line-height:50px;letter-spacing:.5px}
.section-title{position:absolute;height:34px;background:var(--blue);color:var(--white);font-family:"Tinos",serif;font-weight:700;font-size:17px;line-height:34px;padding-left:38px}
.list{position:absolute;list-style:none;font-size:13px;line-height:17.2px;color:var(--text)}
.list li{padding-left:42px;position:relative}
.list li::before{content:"";position:absolute;left:4px;top:5px;width:6px;height:6px;border:1.3px solid var(--text);border-radius:50%}
.split{position:absolute;left:490px;top:950px;width:368px;border-collapse:collapse;font-size:12px;border:2px solid #333;background:var(--white)}
.split th{background:var(--deep);color:var(--white);font-weight:400;font-size:10px;text-align:left;padding:4px 8px}
.split th:last-child,.split td:last-child{text-align:center}
.split td{padding:3px 8px;border-top:1px solid #333}
.phone{position:absolute;left:0;width:902px;top:1102px;text-align:center;color:var(--white);font-size:44px;letter-spacing:1px;line-height:60px}
</style>
</head>
<body>
<main class="flyer">
  <div class="hero-photo" role="img" aria-label="Photo of a tall glass office tower against a cloudy sky"></div>
  <svg class="hero-shapes" viewBox="0 0 902 600" aria-hidden="true">
    <path d="M0 0H902V70H470L430 105H0Z" fill="var(--sky)"/>
    <path d="M0 105H430L470 70H902V95H490L455 125H0Z" fill="var(--white)" opacity=".85"/>
    <path d="M490 130L530 95H902V110H545L510 140Z" fill="var(--blue)"/>
    <path d="M420 140L455 110H520L485 140Z" fill="var(--sky)"/>
    <path d="M0 455C220 540 600 545 902 470V560H0Z" fill="var(--blue)"/>
    <path d="M0 470C250 540 600 530 902 455V480C600 550 250 555 0 488Z" fill="var(--white)" opacity=".9"/>
    <path d="M0 560H902V600H0Z" fill="var(--white)"/>
  </svg>

  <div class="contact">https://www.harborkeyrealty.com.<br>info@harborkeyrealty.com.</div>
  <div class="brand">HARBOR KEY REALTY</div>

  <h1 class="headline">HKR HOME CENTER GAITHERSBURG,<br>MARYLAND IS NOW OPEN!</h1>

  <h2 class="pitch">IGNITE YOUR REAL ESTATE BUSINESS<br>JOIN HARBOR KEY REALTY</h2>

  <h3 class="section-title" style="left:40px;top:715px;width:372px">CONSUMER DIRECT ADVANTAGE</h3>
  <ul class="list" style="left:40px;top:765px">
    <li>Lender Referrals</li>
    <li>Listora Leads</li>
    <li>Shared Lender Leads</li>
    <li>HomeFinderHub.com / NearbyHomesList.com</li>
    <li>Credit Trigger Campaigns</li>
    <li>Consumer Behavior Campaigns</li>
    <li>HKR Call Center Marketing Team</li>
    <li>HKR Sponsored Local Events</li>
  </ul>

  <h3 class="section-title" style="left:490px;top:715px;width:412px">COMPLETE SUPPORT SYSTEM</h3>
  <ul class="list" style="left:490px;top:765px">
    <li>Powerful Suite of Cloud Based Tools</li>
    <li>IDX, CRM and Transaction Management</li>
    <li>HKR Call Center Support for Leads and Deals</li>
    <li>Transaction Coordinator</li>
    <li>Virtual Assistants Available</li>
    <li>24/7 Workspace Access</li>
    <li>Coaching / Mentoring</li>
    <li>Social Media / Marketing Expertise</li>
    <li>Nationwide Partnerships with Top Lenders</li>
  </ul>

  <h3 class="section-title" style="left:40px;top:948px;width:340px">MAXIMIZED COMPENSATION</h3>
  <ul class="list" style="left:40px;top:998px">
    <li>No desk fees. No royalty fees. No franchise fees.</li>
    <li>Company paid E&amp;O</li>
    <li>Transaction fee of $550 includes Transaction Coordinator</li>
  </ul>

  <table class="split">
    <tr><th>TYPE OF DEAL</th><th>COMMISSION SPLIT</th></tr>
    <tr><td>Self-Generated</td><td>90% / 10%</td></tr>
    <tr><td>Lender Referred Leads</td><td>70% / 30%</td></tr>
    <tr><td>HKR Generated Leads / Referrals</td><td>55% / 45%</td></tr>
  </table>

  <svg style="position:absolute;left:0;top:1085px" width="902" height="115" viewBox="0 0 902 115" aria-hidden="true">
    <path d="M0 10H210L225 0H902V6H232L218 18H0Z" fill="var(--sky)" opacity=".7"/>
    <path d="M0 22H902V30H0Z" fill="var(--sky)" opacity=".35"/>
    <path d="M200 20H730L760 80H170Z" fill="var(--blue)"/>
    <path d="M0 80H902V115H0Z" fill="var(--white)"/>
    <path d="M0 84H330V90H0ZM570 84H902V90H570Z" fill="var(--sky)"/>
  </svg>
  <div class="phone">+1 866 555 0148</div>
</main>
</body>
</html>
```